Simplified Double Diamond Diagram for Book

I need a simplified version of the Double Diamond Diagram for a book I am working on. I would like to represent the diagram with the following image/text:
- Two diamonds connected (as in each of the sample photos)
- Inclusion of "Diverge" "Converge" above each of the sides of the diamonds as shown in sample image 1 - without elaborative text
- Inclusion of "Problem" and "Solution" in each diamond as is shown in the example image 2
- I need a color version and black/white version of the image that can be turned into a mono-color version in the book.

```html
<!DOCTYPE html>
<html lang="en">
<head>
<meta charset="utf-8">
<title>Double Diamond Diagram – Colour and Mono Versions</title>
<link rel="stylesheet" href="https://fonts.googleapis.com/css2?family=Montserrat:wght@300;800&display=swap">
<style>
  :root {
    --paper: #ffffff;
    --green-light: #bbe0c5;
    --green: #48b064;
    --olive: #77622b;
    --blue-light: #a6ddef;
    --blue: #318fc1;
    --navy: #163663;
    --grey-light: #d1d2d4;
    --grey-mid: #9a9b9e;
    --grey-edge: #6d6e71;
    --grey-light-2: #cfd0d2;
    --grey-dark: #8a8b8e;
    --grey-edge-dark: #4a4a4c;
    --ink: #231f20;
    --caption: #939598;
    --divider: #77622b;
  }
  html, body {
    margin: 0;
    padding: 0;
    overflow: hidden;
    background: var(--paper);
  }
  .canvas {
    display: block;
    width: 1200px;
    height: 1200px;
  }
  .edge-label {
    font-family: "Montserrat", sans-serif;
    font-weight: 800;
    font-size: 27px;
    text-anchor: middle;
    dominant-baseline: central;
  }
  .phase-label {
    font-family: "Montserrat", sans-serif;
    font-weight: 800;
    font-size: 27px;
    text-anchor: middle;
    dominant-baseline: central;
  }
  .caption {
    font-family: "Montserrat", sans-serif;
    font-weight: 300;
    font-size: 25px;
    fill: var(--caption);
    text-anchor: middle;
  }
  .option-label {
    font-family: "Montserrat", sans-serif;
    font-weight: 300;
    font-size: 24px;
    fill: #58595b;
    text-anchor: middle;
  }
  .divider {
    stroke: var(--divider);
    stroke-width: 2;
    stroke-dasharray: 10 7;
  }
  .outline { stroke-width: 8; stroke-linejoin: miter; }
  .on-olive { fill: var(--olive); }
  .on-navy { fill: var(--navy); }
  .on-grey { fill: var(--grey-edge); }
  .on-grey-dark { fill: var(--grey-edge-dark); }
  .on-ink { fill: var(--ink); }
  .on-white { fill: var(--paper); }
  .centre-dots {
    stroke: var(--ink);
    stroke-width: 8;
    stroke-dasharray: 8 8;
  }
</style>
</head>
<body>
<svg class="canvas" viewBox="0 0 1920 1920" xmlns="http://www.w3.org/2000/svg" role="img" aria-label="Double Diamond diagram: Problem and Solution, each with Diverge and Converge, in colour, greyscale and black-and-white versions">
  <defs>
    <clipPath id="left-half"><rect x="-200" y="-200" width="200" height="400"/></clipPath>
    <clipPath id="right-half"><rect x="0" y="-200" width="200" height="400"/></clipPath>
  </defs>

  <!-- Option 1 -->
  <g class="option option-1">
    <g class="diamond problem colour" transform="translate(328 279)">
      <path d="M0,-190 L0,190 L-190,0 Z" fill="var(--green-light)"/>
      <path d="M0,-190 L190,0 L0,190 Z" fill="var(--green)"/>
      <path class="outline" d="M0,-190 L190,0 L0,190 L-190,0 Z" fill="none" stroke="var(--olive)"/>
      <text class="edge-label on-olive" transform="translate(-113 -111) rotate(-45)">DIVERGE</text>
      <text class="edge-label on-olive" transform="translate(112 -111) rotate(45)">CONVERGE</text>
      <text class="phase-label on-white" x="0" y="-6">PROBLEM</text>
    </g>
    <g class="diamond solution colour" transform="translate(708 279)">
      <path d="M0,-190 L0,190 L-190,0 Z" fill="var(--blue-light)"/>
      <path d="M0,-190 L190,0 L0,190 Z" fill="var(--blue)"/>
      <path class="outline" d="M0,-190 L190,0 L0,190 L-190,0 Z" fill="none" stroke="var(--navy)"/>
      <text class="edge-label on-navy" transform="translate(-113 -111) rotate(-45)">DIVERGE</text>
      <text class="edge-label on-navy" transform="translate(112 -111) rotate(45)">CONVERGE</text>
      <text class="phase-label on-white" x="0" y="-6">SOLUTION</text>
    </g>
    <text class="caption" x="500" y="520">Color Version</text>

    <g class="diamond problem greyscale" transform="translate(1198 279)">
      <path d="M0,-190 L0,190 L-190,0 Z" fill="var(--grey-light)"/>
      <path d="M0,-190 L190,0 L0,190 Z" fill="var(--grey-mid)"/>
      <path class="outline" d="M0,-190 L190,0 L0,190 L-190,0 Z" fill="none" stroke="var(--grey-edge)"/>
      <text class="edge-label on-grey" transform="translate(-113 -111) rotate(-45)">DIVERGE</text>
      <text class="edge-label on-grey" transform="translate(112 -111) rotate(45)">CONVERGE</text>
      <text class="phase-label on-white" x="0" y="-8">PROBLEM</text>
    </g>
    <g class="diamond solution greyscale" transform="translate(1578 279)">
      <path d="M0,-190 L0,190 L-190,0 Z" fill="var(--grey-light-2)"/>
      <path d="M0,-190 L190,0 L0,190 Z" fill="var(--grey-dark)"/>
      <path class="outline" d="M0,-190 L190,0 L0,190 L-190,0 Z" fill="none" stroke="var(--grey-edge-dark)"/>
      <text class="edge-label on-grey-dark" transform="translate(-113 -111) rotate(-45)">DIVERGE</text>
      <text class="edge-label on-grey-dark" transform="translate(112 -111) rotate(45)">CONVERGE</text>
      <text class="phase-label on-white" x="0" y="-8">SOLUTION</text>
    </g>
    <text class="caption" x="1374" y="520">Grey Scale (Halftone) (Mono Color)</text>
    <text class="option-label" transform="translate(76 520) rotate(-90)">Optin 1</text>
  </g>
  <line class="divider" x1="76" y1="598" x2="1874" y2="598"/>

  <!-- Option 2 -->
  <g class="option option-2">
    <g class="diamond problem colour" transform="translate(328 864)">
      <path d="M0,-190 L0,190 L-190,0 Z" fill="var(--green-light)"/>
      <path d="M0,-190 L190,0 L0,190 Z" fill="var(--green)"/>
      <path class="outline" d="M0,-190 L190,0 L0,190 L-190,0 Z" fill="none" stroke="var(--olive)"/>
      <text class="edge-label on-olive" transform="translate(-113 -111) rotate(-45)">DIVERGE</text>
      <text class="edge-label on-olive" transform="translate(112 -111) rotate(45)">CONVERGE</text>
      <text class="phase-label on-white" x="0" y="-6">PROBLEM</text>
    </g>
    <g class="diamond solution colour" transform="translate(708 864)">
      <path d="M0,-190 L0,190 L-190,0 Z" fill="var(--blue-light)"/>
      <path d="M0,-190 L190,0 L0,190 Z" fill="var(--blue)"/>
      <path class="outline" d="M0,-190 L190,0 L0,190 L-190,0 Z" fill="none" stroke="var(--navy)"/>
      <text class="edge-label on-navy" transform="translate(-113 -111) rotate(-45)">DIVERGE</text>
      <text class="edge-label on-navy" transform="translate(112 -111) rotate(45)">CONVERGE</text>
      <text class="phase-label on-white" x="0" y="-6">SOLUTION</text>
    </g>
    <text class="caption" x="500" y="1100">Color Version</text>

    <g class="diamond problem black-white" transform="translate(1198 864)">
      <path d="M0,-190 L0,190 L-190,0 Z" fill="var(--ink)"/>
      <path d="M0,-190 L190,0 L0,190 Z" fill="var(--paper)"/>
      <path class="outline" d="M0,-190 L190,0 L0,190 L-190,0 Z" fill="none" stroke="var(--ink)"/>
      <text class="edge-label on-ink" transform="translate(-113 -111) rotate(-45)">DIVERGE</text>
      <text class="edge-label on-ink" transform="translate(112 -111) rotate(45)">CONVERGE</text>
      <text class="phase-label on-white" x="0" y="-10" clip-path="url(#left-half)">PROBLEM</text>
      <text class="phase-label on-ink" x="0" y="-10" clip-path="url(#right-half)">PROBLEM</text>
    </g>
    <g class="diamond solution black-white" transform="translate(1578 864)">
      <path d="M0,-190 L0,190 L-190,0 Z" fill="var(--ink)"/>
      <path d="M0,-190 L190,0 L0,190 Z" fill="var(--paper)"/>
      <path class="outline" d="M0,-190 L190,0 L0,190 L-190,0 Z" fill="none" stroke="var(--ink)"/>
      <text class="edge-label on-ink" transform="translate(-113 -111) rotate(-45)">DIVERGE</text>
      <text class="edge-label on-ink" transform="translate(112 -111) rotate(45)">CONVERGE</text>
      <text class="phase-label on-white" x="0" y="-8" clip-path="url(#left-half)">SOLUTION</text>
      <text class="phase-label on-ink" x="0" y="-8" clip-path="url(#right-half)">SOLUTION</text>
    </g>
    <text class="caption" x="1393" y="1100">Black-White Solid (Mono Color)</text>
    <text class="option-label" transform="translate(76 1115) rotate(-90)">Optin 2</text>
  </g>
  <line class="divider" x1="76" y1="1171" x2="1874" y2="1171"/>

  <!-- Option 3 -->
  <g class="option option-3">
    <g class="diamond problem colour" transform="translate(328 1449)">
      <path d="M0,-190 L0,190 L-190,0 Z" fill="var(--green-light)"/>
      <path d="M0,-190 L190,0 L0,190 Z" fill="var(--green)"/>
      <path class="outline" d="M0,-190 L190,0 L0,190 L-190,0 Z" fill="none" stroke="var(--olive)"/>
      <text class="edge-label on-olive" transform="translate(-113 -111) rotate(-45)">DIVERGE</text>
      <text class="edge-label on-olive" transform="translate(112 -111) rotate(45)">CONVERGE</text>
      <text class="phase-label on-white" x="0" y="-6">PROBLEM</text>
    </g>
    <g class="diamond solution colour" transform="translate(708 1449)">
      <path d="M0,-190 L0,190 L-190,0 Z" fill="var(--blue-light)"/>
      <path d="M0,-190 L190,0 L0,190 Z" fill="var(--blue)"/>
      <path class="outline" d="M0,-190 L190,0 L0,190 L-190,0 Z" fill="none" stroke="var(--navy)"/>
      <text class="edge-label on-navy" transform="translate(-113 -111) rotate(-45)">DIVERGE</text>
      <text class="edge-label on-navy" transform="translate(112 -111) rotate(45)">CONVERGE</text>
      <text class="phase-label on-white" x="0" y="-6">SOLUTION</text>
    </g>
    <text class="caption" x="500" y="1692">Color Version</text>

    <g class="diamond problem line-drawing" transform="translate(1198 1449)">
      <path class="outline" d="M0,-190 L190,0 L0,190 L-190,0 Z" fill="var(--paper)" stroke="var(--ink)"/>
      <line class="centre-dots" x1="0" y1="-180" x2="0" y2="-24"/>
      <line class="centre-dots" x1="0" y1="14" x2="0" y2="180"/>
      <text class="edge-label on-ink" transform="translate(-113 -111) rotate(-45)">DIVERGE</text>
      <text class="edge-label on-ink" transform="translate(112 -111) rotate(45)">CONVERGE</text>
      <text class="phase-label on-ink" x="0" y="-8">PROBLEM</text>
    </g>
    <g class="diamond solution line-drawing" transform="translate(1578 1449)">
      <path class="outline" d="M0,-190 L190,0 L0,190 L-190,0 Z" fill="var(--paper)" stroke="var(--ink)"/>
      <line class="centre-dots" x1="0" y1="-180" x2="0" y2="-24"/>
      <line class="centre-dots" x1="0" y1="14" x2="0" y2="180"/>
      <text class="edge-label on-ink" transform="translate(-113 -111) rotate(-45)">DIVERGE</text>
      <text class="edge-label on-ink" transform="translate(112 -111) rotate(45)">CONVERGE</text>
      <text class="phase-label on-ink" x="0" y="-8">SOLUTION</text>
    </g>
    <text class="caption" x="1393" y="1692">Black-White Solid Line Drawing (Mono Color))</text>
    <text class="option-label" transform="translate(76 1700) rotate(-90)">Optin 3</text>
  </g>
  <line class="divider" x1="76" y1="1741" x2="1874" y2="1741"/>
</svg>
</body>
</html>
```